Website for Community Storage Startup Company

We're looking for a great design that looks good on mobile devices (as well as the web) - Layout should be responsive and able to scale to many sized devices.

It should provide a good user-experience for people browsing the site with heavy focus on search and search results pages - It should be extremely easy to search, see results and add your own information.

Search parameters should be Location (Text), Dates (Calendar pop up), Price (slider) with optional extra parameters to be displayed (You can just call them Parameter1, Parameter2 etc. for Examples- we'd like to see options of no extra parameters and up to 4 others)

Please include a favicon for the site - we've provided the logo we had designed.

Pages We Must Have:

1) Home Page
2) Search Page (most likely map based)
3) Search Results Page (most likely map based) - we want the search options/results to slide in and out as appropriate - please visualize
Information Page - this is branded and would present information for many possible pages like Terms & Conditions or a FAQ page etc.
4) My Account Page - Should be an inline editable page with Name/Address/Financial information etc. showing
5) Sign-up Page - This could be a slide in element on another page or part of the account page, or separate as you think works best

Ideally this would all work like a single page app with a common theme but we're interested to see your ideas of tying pages together or keeping them separate while fitting our brief.

Examples of things we like;

a) roostly - mobile and web based layouts - we like the map on the side and data input on the other side
b) http://www.zu-o.com/zo/airlines/ - scroll down slightly to the first video - about 0:28 in we like the map on the side and the panel on the side with details you can refine etc. All over we like the site presented through the video

Nice to Have:
- The ability to provide the finished design as sliced CSS, HTML and JS

Reason: Feedback has suggested that the timeline is too tight, we've extended it but are very interested in seeing initial page designs sooner rather than later to provide feedback. Thanks!

Thanks for your contributions so far :)  We've come to realize that in general we're preferring darker color schemes - if you're pulling colors from our logo try to stick to the text colors :)

We like narrow headers and footers and a map based interface. Sliders for information are good and we'd like to see how checkbox elements would play out too.

Examples of how information may pop up from markers would be nice too.

Thanks for everything so far!

Target Market(s)

Young to middle aged adults in the USA

Industry/Entity Type

Airlines

Font styles to use
Sans Serif

Colors

Designer to choose colors to be used in the design.

Requirements
Must have
• 1) Home Page
Nice to have
• The ability to provide the finished design as sliced CSS, HTML and JS

We think a map with markers should figure heavily in search results and searching.

```html
<!DOCTYPE html>
<html lang="en">
<head>
<meta charset="utf-8">
<title>Stowvio – Community Storage</title>
<link href="https://fonts.googleapis.com/css2?family=Open+Sans:wght@300;400;600&family=Noticia+Text&display=swap" rel="stylesheet">
<style>
:root{
  --lavender:#9e9ad0;
  --link:#9a96c8;
  --ink:#333;
  --muted:#666;
  --icon:#666;
  --footer-bg:#f3f3f3;
  --bar-bg:#2a2a2a;
  --field-border:#dcdcdc;
}
*{box-sizing:border-box;margin:0;padding:0}
html,body{width:1104px;height:1200px;overflow:hidden;background:#fff;font-family:"Open Sans",Arial,sans-serif;color:var(--ink)}
.page{position:relative;width:1104px;height:1200px}
.abs{position:absolute}

.brand{left:92px;top:56px;display:flex;align-items:center;gap:12px;font-size:40px;font-weight:400;color:#2b2b2b;letter-spacing:.5px}
.brand-mark{width:22px;height:22px;background:var(--lavender)}
.account-links{right:92px;top:42px;font-size:14px;color:var(--link);display:flex;gap:10px}
.account-links .sep{color:#bbb}
.list-space{left:821px;top:87px;width:191px;height:39px;border-radius:3px;background:linear-gradient(#b4b1e2,#9894d0);color:#fff;font-size:16px;font-weight:600;display:flex;align-items:center;justify-content:center;text-shadow:0 1px 1px rgba(0,0,0,.25)}

.hero{left:0;top:154px;width:1104px;height:436px;
  background:
    radial-gradient(ellipse 22% 30% at 74% 22%, rgba(200,205,215,.55), transparent 70%),
    radial-gradient(ellipse 18% 22% at 24% 78%, rgba(190,150,110,.55), transparent 70%),
    radial-gradient(ellipse 20% 25% at 45% 20%, rgba(160,120,90,.45), transparent 70%),
    linear-gradient(135deg,#3b3836 0%,#5e5248 35%,#6f6358 55%,#44413f 80%,#2a2929 100%)}
.hero-title{left:0;top:316px;width:1104px;text-align:center;color:#fff;font-size:39px;font-weight:400;text-shadow:0 2px 4px rgba(0,0,0,.6)}
.hero-arrow{top:356px;width:24px;height:34px}
.search-bar{left:123px;top:370px;width:823px;height:45px;background:#222;border-radius:2px}
.field{top:376px;height:35px;background:#fff;border-radius:2px;font-size:13px;color:#555;display:flex;align-items:center;padding-left:14px}
.slider-track{position:absolute;left:52px;top:15px;width:152px;height:6px;border-radius:3px;background:#aaa}
.slider-knob{position:absolute;left:97px;top:11px;width:14px;height:14px;border-radius:50%;background:var(--lavender);border:2px solid #ddd}
.price-val{position:absolute;right:10px;top:9px;font-size:12px}
.search-btn{left:941px;top:374px;width:40px;height:38px;border-radius:3px;background:var(--lavender);display:flex;align-items:center;justify-content:center}

.tagline{left:0;top:628px;width:1104px;text-align:center;font-family:"Noticia Text",Georgia,serif;font-size:23.5px;font-weight:400;color:var(--lavender)}
.feature-photo{top:695px;width:288px;height:145px}
.feature-caption{top:850px;width:288px;text-align:center;font-size:16px;font-weight:300;color:var(--link)}

.footer{left:0;top:909px;width:1104px;height:235px;background:var(--footer-bg)}
.footer h3{position:absolute;font-size:14px;font-weight:400;color:#222}
.footer ul{position:absolute;list-style:none;font-size:12px;color:var(--muted);line-height:23px}
.social{position:absolute;top:192px;left:112px;display:flex;gap:6px}
.social span{width:26px;height:27px;border:1px solid #c9c9c9;border-radius:3px;background:#fff;display:flex;align-items:center;justify-content:center}
.input{position:absolute;left:714px;width:213px;background:#fff;border:1px solid var(--field-border);border-radius:2px;font-size:12px;color:#444;padding:9px 11px}
.submit{position:absolute;left:935px;top:176px;width:60px;height:30px;border-radius:3px;background:#555;color:#eee;font-size:12px;display:flex;align-items:center;justify-content:center}
.bottom-bar{left:0;top:1144px;width:1104px;height:56px;background:var(--bar-bg);color:#999;font-size:12px;display:flex;align-items:center;justify-content:center}
</style>
</head>
<body>
<div class="page">
  <header>
    <div class="abs brand"><span class="brand-mark"></span>Stowvio</div>
    <nav class="abs account-links"><span>REGISTER</span><span class="sep">/</span><span>LOG IN</span><span class="sep">/</span><span>HELP</span></nav>
    <div class="abs list-space">LIST YOUR SPACE</div>
  </header>

  <section>
    <div class="abs hero" role="img" aria-label="Photo of a cluttered garage full of boxes, bikes and stored household items"></div>
    <h1 class="abs hero-title">MAURIS A VEHICULA LEO</h1>
    <svg class="abs hero-arrow" style="left:18px" viewBox="0 0 24 34"><path d="M18 3 5 17l13 14" fill="none" stroke="#fff" stroke-width="3"/></svg>
    <svg class="abs hero-arrow" style="left:1064px" viewBox="0 0 24 34"><path d="M6 3l13 14L6 31" fill="none" stroke="#fff" stroke-width="3"/></svg>
    <div class="abs search-bar"></div>
    <div class="abs field" style="left:130px;width:210px">Location</div>
    <div class="abs field" style="left:345px;width:143px">Dates
      <svg style="position:absolute;right:8px;top:6px" width="25" height="24" viewBox="0 0 25 24"><rect x="1" y="3" width="23" height="20" fill="#fff" stroke="#999"/><rect x="1" y="3" width="23" height="5" fill="#999"/><g fill="#aaa"><rect x="4" y="10" width="3" height="3"/><rect x="9" y="10" width="3" height="3"/><rect x="14" y="10" width="3" height="3"/><rect x="19" y="10" width="3" height="3"/><rect x="4" y="15" width="3" height="3"/><rect x="9" y="15" width="3" height="3"/><rect x="14" y="15" width="3" height="3"/><rect x="19" y="15" width="3" height="3"/></g></svg>
    </div>
    <div class="abs field" style="left:492px;width:258px">Price<span class="slider-track"></span><span class="slider-knob"></span><span class="price-val">$00.00</span></div>
    <div class="abs field" style="left:755px;width:182px">Parameter1
      <svg style="position:absolute;right:8px;top:13px" width="14" height="9" viewBox="0 0 14 9"><path d="M0 0h14L7 9z" fill="#999"/></svg>
    </div>
    <div class="abs search-btn"><svg width="18" height="18" viewBox="0 0 18 18"><circle cx="7" cy="7" r="5" fill="none" stroke="#fff" stroke-width="2.2"/><path d="M11 11l5 5" stroke="#fff" stroke-width="2.6"/></svg></div>
  </section>

  <section>
    <h2 class="abs tagline">Vestibulum urna nunc, facilisis non pretium sed, tincidunt interdum nisi.</h2>
    <div class="abs feature-photo" style="left:101px;background:radial-gradient(ellipse 40% 35% at 70% 75%,rgba(235,228,215,.8),transparent 70%),radial-gradient(ellipse 35% 40% at 15% 35%,rgba(150,170,120,.6),transparent 70%),linear-gradient(135deg,#6e5a48,#9a7e64 50%,#4f3e30)" role="img" aria-label="Photo of a cosy living room with sofa and coffee table"></div>
    <div class="abs feature-photo" style="left:408px;background:radial-gradient(ellipse 45% 40% at 50% 45%,rgba(40,40,40,.85),transparent 75%),radial-gradient(ellipse 40% 30% at 55% 85%,rgba(170,140,170,.6),transparent 70%),linear-gradient(180deg,#ececec,#cfcfcf 60%,#d8d2cc)" role="img" aria-label="Photo of a leather sofa piled with clothes"></div>
    <div class="abs feature-photo" style="left:715px;background:radial-gradient(ellipse 30% 50% at 50% 60%,rgba(110,130,160,.6),transparent 70%),radial-gradient(ellipse 25% 30% at 10% 75%,rgba(90,200,210,.6),transparent 70%),linear-gradient(135deg,#e3d2b4,#c9a77c 50%,#d6b891)" role="img" aria-label="Photo of a couple sitting among moving boxes"></div>
    <p class="abs feature-caption" style="left:101px">Integer congue elementum</p>
    <p class="abs feature-caption" style="left:408px">Phasellus lacinia auctor</p>
    <p class="abs feature-caption" style="left:715px">Mauris a vehicula</p>
  </section>

  <footer class="abs footer">
    <h3 style="left:111px;top:30px">Navigation Menu</h3>
    <ul style="left:111px;top:58px"><li>Home</li><li>About us</li><li>Services</li><li>Our Works</li></ul>
    <ul style="left:208px;top:58px"><li>Contact us</li><li>Register</li><li>Login</li></ul>
    <h3 style="left:351px;top:30px">Support Links</h3>
    <ul style="left:351px;top:58px"><li>Privacy Policy</li><li>Terms and Conditions</li><li>Customer Support</li><li>FAQ</li></ul>
    <h3 style="left:563px;top:30px">About us</h3>
    <ul style="left:563px;top:58px"><li>Who we are</li><li>What we do</li><li>Our Projects</li><li>Our History</li></ul>
    <h3 style="left:717px;top:30px">Contact us</h3>
    <div class="social">
      <span aria-label="Share"><svg width="12" height="12" viewBox="0 0 12 12"><circle cx="2.5" cy="6" r="1.8" fill="var(--icon)"/><circle cx="9.5" cy="2.5" r="1.8" fill="var(--icon)"/><circle cx="9.5" cy="9.5" r="1.8" fill="var(--icon)"/><path d="M2.5 6 9.5 2.5M2.5 6l7 3.5" stroke="var(--icon)" stroke-width="1.2"/></svg></span>
      <span aria-label="Link"><svg width="13" height="13" viewBox="0 0 13 13"><rect x="1" y="4" width="6" height="5" rx="2.5" fill="none" stroke="var(--icon)" stroke-width="1.4"/><rect x="6" y="4" width="6" height="5" rx="2.5" fill="none" stroke="var(--icon)" stroke-width="1.4"/></svg></span>
      <span aria-label="Profile"><svg width="12" height="12" viewBox="0 0 12 12"><circle cx="6" cy="3.5" r="2.5" fill="var(--icon)"/><path d="M1 12a5 4.5 0 0 1 10 0z" fill="var(--icon)"/></svg></span>
      <span aria-label="Email"><svg width="14" height="10" viewBox="0 0 14 10"><rect x=".5" y=".5" width="13" height="9" fill="none" stroke="var(--icon)"/><path d="M.5 .5 7 6l6.5-5.5" fill="none" stroke="var(--icon)"/></svg></span>
      <span aria-label="Feed"><svg width="12" height="12" viewBox="0 0 12 12"><circle cx="2" cy="10" r="1.6" fill="var(--icon)"/><path d="M1 5a6 6 0 0 1 6 6M1 1a10 10 0 0 1 10 10" fill="none" stroke="var(--icon)" stroke-width="1.6"/></svg></span>
    </div>
    <div class="input" style="top:67px;height:33px">Name</div>
    <div class="input" style="top:106px;height:33px">E-mail</div>
    <div class="input" style="top:145px;height:61px">Comment</div>
    <div class="submit">SUBMIT</div>
  </footer>
  <div class="abs bottom-bar">Copyright © 2014 Stowvio.&nbsp;&nbsp;All rights reserved.</div>
</div>
</body>
</html>
```